Brightwater Health Partners, LLC Business Card update!

would like a classier business card. Our cards currently just have our logo and contact information. Need better use of color and creativity
Logo attached.

Target Market(s)

Potential clients, contacts, existing clients. We are a consulting company

Industry/Entity Type

Business

Contact Information for Business Card

We like our colors but just have a boring card with our logo and a white background. I want something that stands out.

Colors
ec1f27
757575

Requirements
Must have
• Color to stay consistent. Logo provided
Nice to have
• Just better use of color/ design

```html
<!DOCTYPE html>
<html lang="en">
<head>
<meta charset="utf-8">
<title>Brightwater Health Partners – Business Card</title>
<link href="https://fonts.googleapis.com/css2?family=Open+Sans:wght@400;600;700&display=swap" rel="stylesheet">
<style>
  :root {
    --brand-red: #ec1f27;
    --brand-grey: #757575;
    --card-black: #050505;
    --page-bg: #1c1c1c;
    --text-light: #e6e6e6;
    --rule: #2e2e2e;
  }
  * { box-sizing: border-box; margin: 0; padding: 0; }
  html, body {
    width: 1200px;
    height: 900px;
    overflow: hidden;
    background: var(--page-bg);
    font-family: "Open Sans", Arial, sans-serif;
  }
  .canvas {
    position: relative;
    width: 1200px;
    height: 900px;
  }
  .business-card {
    position: absolute;
    left: 180px;
    top: 210px;
    width: 840px;
    height: 480px;
    background: var(--card-black);
    box-shadow: 0 18px 40px rgba(0,0,0,.6);
  }
  .brand {
    position: absolute;
    top: 92px;
    right: 70px;
    display: flex;
    align-items: center;
    gap: 16px;
  }
  .brand-mark {
    width: 54px;
    height: 54px;
    border-radius: 50%;
    border: 5px solid var(--brand-grey);
  }
  .brand-name {
    color: var(--brand-red);
    font-weight: 600;
    font-size: 30px;
    line-height: 1.1;
    letter-spacing: .3px;
  }
  .divider {
    position: absolute;
    left: 340px;
    right: 70px;
    top: 232px;
    height: 1px;
    background: var(--rule);
  }
  .holder {
    position: absolute;
    left: 96px;
    top: 212px;
  }
  .holder-name {
    color: #ffffff;
    font-weight: 700;
    font-size: 22px;
    line-height: 1.2;
  }
  .holder-title {
    color: var(--brand-red);
    font-size: 18px;
    line-height: 1.3;
  }
  .contact-list {
    position: absolute;
    right: 64px;
    top: 260px;
    list-style: none;
    text-align: right;
  }
  .contact-item {
    display: flex;
    justify-content: flex-end;
    align-items: center;
    gap: 14px;
    color: var(--text-light);
    font-size: 16px;
    line-height: 30px;
  }
  .contact-icon {
    width: 16px;
    height: 16px;
    flex: none;
    fill: var(--brand-red);
  }
</style>
</head>
<body>
<div class="canvas">
  <section class="business-card">
    <div class="brand">
      <span class="brand-mark"></span>
      <span class="brand-name">Brightwater<br>Health Partners</span>
    </div>

    <div class="divider"></div>

    <div class="holder">
      <p class="holder-name">Owner Name</p>
      <p class="holder-title">Managing Director</p>
    </div>

    <ul class="contact-list">
      <li class="contact-item">000 123 456 456
        <svg class="contact-icon" viewBox="0 0 16 16" aria-hidden="true"><path d="M1 5c0-2 3-3 7-3s7 1 7 3v1h-4V4.5H5V6H1z"/><path d="M3 8h10l1 6H2z"/></svg>
      </li>
      <li class="contact-item">iinfo@compnayname.com
        <svg class="contact-icon" viewBox="0 0 16 16" aria-hidden="true"><path d="M1 3h14v1.5L8 9 1 4.5z"/><path d="M1 6.5 8 11l7-4.5V13H1z"/></svg>
      </li>
      <li class="contact-item">www.companyname.com
        <svg class="contact-icon" viewBox="0 0 16 16" aria-hidden="true"><path d="M6.5 9.5 9.5 6.5" stroke="#ec1f27" stroke-width="2" fill="none"/><rect x="1.5" y="8" width="7" height="4" rx="2" transform="rotate(-45 5 10)" stroke="#ec1f27" stroke-width="1.8" fill="none"/><rect x="7.5" y="4" width="7" height="4" rx="2" transform="rotate(-45 11 6)" stroke="#ec1f27" stroke-width="1.8" fill="none"/></svg>
      </li>
      <li class="contact-item">Address line1, Address Line, Country, 012
        <svg class="contact-icon" viewBox="0 0 16 16" aria-hidden="true"><path d="M8 1a5 5 0 0 0-5 5c0 4 5 9 5 9s5-5 5-9a5 5 0 0 0-5-5zm0 7a2 2 0 1 1 0-4 2 2 0 0 1 0 4z"/></svg>
      </li>
    </ul>
  </section>
</div>
</body>
</html>
```